Magazine Design Project

I need a magazine that will describe the fashion street style in london,also the style I want to be like zine magazine.

Fashion

```html
<!DOCTYPE html>
<html lang="en">
<head>
<meta charset="utf-8">
<title>rush — how the city looks</title>
<link rel="stylesheet" href="https://fonts.googleapis.com/css2?family=Arimo:wght@400&display=swap">
<style>
  :root {
    --backdrop: #e6e6e6;
    --paper: #ffffff;
    --ink: #111111;
    --accent: #e8413f;
    --accent-tint: rgba(240, 80, 80, 0.72);
    --photo-light: #d9d9d9;
    --photo-mid: #8c8c8c;
    --photo-dark: #3a3a3a;
    --rule: #8a8a8a;
  }
  * { box-sizing: border-box; margin: 0; padding: 0; }
  html, body { width: 951px; height: 1200px; overflow: hidden; }
  body {
    background: var(--backdrop);
    font-family: "Arimo", Arial, sans-serif;
    font-weight: 400;
    position: relative;
  }
  h1, h2 { font-weight: 400; }
  .sheet {
    position: absolute;
    background: var(--paper);
    box-shadow: 0 2px 8px rgba(0,0,0,0.18);
    overflow: hidden;
  }

  /* Cover */
  .cover { left: 310px; top: 60px; width: 331px; height: 469px; }
  .cover__photo {
    position: absolute; left: 17px; top: 21px; width: 296px; height: 430px;
    background: linear-gradient(160deg, var(--photo-light) 0%, #bdbdbd 45%, var(--photo-mid) 75%, #c9c9c9 100%);
  }
  .cover__block {
    position: absolute; left: 82px; top: 123px; width: 179px; height: 180px;
    background: var(--accent-tint);
  }
  .cover__title {
    position: absolute; left: 30px; top: 362px;
    font-size: 48px; line-height: 1; color: var(--accent);
  }
  .cover__tagline {
    position: absolute; left: 160px; top: 388px; width: 137px;
    font-size: 14px; line-height: 16px; color: var(--accent); text-align: right;
  }

  /* Inner pages */
  .page { top: 650px; width: 330px; height: 468px; }
  .page--jeans { left: 150px; }
  .page--friends { left: 500px; }
  .page__photo {
    position: absolute; left: 14px; top: 34px; width: 304px; height: 203px;
  }
  .page--jeans .page__photo {
    background: linear-gradient(90deg, var(--photo-dark) 0%, var(--photo-mid) 45%, #bcbcbc 60%, var(--photo-dark) 100%);
  }
  .page--friends .page__photo {
    background: linear-gradient(180deg, #2e2e2e 0%, var(--photo-mid) 55%, #b8b8b8 100%);
  }
  .page--friends .page__photo--faded {
    top: 237px; height: 205px;
    background: linear-gradient(180deg, #e4e4e4 0%, #cfcfcf 50%, #ececec 100%);
  }
  .page__guide {
    position: absolute; border: 1px solid var(--rule);
  }
  .page--jeans .page__guide { left: 63px; top: 237px; width: 204px; height: 190px; }
  .page--friends .page__guide { left: 70px; top: 40px; width: 192px; height: 382px; border-color: #b5b5b5; }
  .page__frame {
    position: absolute; left: 83px; top: 50px; width: 166px; height: 366px;
    border: 5px solid var(--ink);
  }
  .page__body {
    position: absolute; left: 92px; top: 246px; width: 149px;
    font-size: 10.5px; line-height: 14px; color: var(--ink);
    white-space: nowrap; overflow: hidden;
  }
  .page__body span { display: block; }
  .page--jeans .page__body { height: 126px; }
  .page--friends .page__body { height: 154px; color: var(--accent); }
  .page__headline {
    position: absolute; left: 92px; top: 372px;
    font-size: 40px; line-height: 1; color: var(--accent);
  }
</style>
</head>
<body>
  <article class="sheet cover">
    <div class="cover__photo" role="img" aria-label="Grainy black and white pencil-textured portrait of a young woman, cover photograph"></div>
    <div class="cover__block"></div>
    <h1 class="cover__title">rush</h1>
    <p class="cover__tagline">how the city looks<br>2013</p>
  </article>

  <article class="sheet page page--jeans">
    <div class="page__photo" role="img" aria-label="Black and white street photo of a woman in denim shorts with a bicycle against a brick wall"></div>
    <div class="page__guide"></div>
    <div class="page__frame"></div>
    <p class="page__body">
      <span>Lorem ipsum dolor sit amet,</span>
      <span>consectetur adipiscing elit. In</span>
      <span>viverra, turpis in placerat</span>
      <span>pulvinar, nulla justo aliquam</span>
      <span>libero, eget faucibus libero nisi</span>
      <span>at sem. Duis vitae urna tortor.</span>
      <span>Sed ut libero augue. Aliquam</span>
      <span>eros magna, ornare ac dapibus</span>
      <span>quis, tincidunt dapibus odio.</span>
    </p>
    <h2 class="page__headline">jeans</h2>
  </article>

  <article class="sheet page page--friends">
    <div class="page__photo" role="img" aria-label="Black and white photo of two young women in sunglasses on a sunny street"></div>
    <div class="page__photo page__photo--faded" role="img" aria-label="Faded light grey street scene photograph"></div>
    <div class="page__guide"></div>
    <div class="page__frame"></div>
    <p class="page__body">
      <span>Lorem ipsum dolor sit amet,</span>
      <span>consectetur adipiscing elit. In</span>
      <span>viverra, turpis in placerat</span>
      <span>pulvinar, nulla justo aliquam</span>
      <span>libero, eget faucibus libero nisi</span>
      <span>at sem. Duis vitae urna tortor.</span>
      <span>Sed ut libero augue. Aliquam</span>
      <span>eros magna, ornare ac dapibus</span>
      <span>quis, tincidunt dapibus odio.</span>
      <span>Praesent turpis augue, ultrices</span>
      <span>vel enim a, gravida consequat</span>
    </p>
  </article>
</body>
</html>
```